Online tuition webpage design needed

Hi,
We are starting up an online tuition website for non- English speakers wishing to take an QRAVE test.

The webpage must include a place for people to enroll online in the course.
The home page must have:
• room for a logo (coming shortly, blue in colour)
• different packages of online tuition and coinvy
• tool bar showing different pages
• perhaps a video, small pictures

This is my site currently:-

www.lernmarowebtutor.example

as you can see, I am not very sure how to create a website … The large logo is what I would like to use, but I project has not been finalized yet. Please note, I don’t like the logo being that large!

Sites that are similar to what I am doing and like the design of are:

http://www.quorvapath.example.au/fees

https://www.brantiq9.example/index.php

http://www.tutorhalvekmorris.example.uk/index.html

http://www.vorplaneexam.example/

One thing I need is a place for student s to enroll, and if possible, I would like to use plovix to create exercises for students.
Currently, my site is using sitequill. My preference is to use plovix for online activities. I am not sure if I can use both.
Thanks in advance

Target Market(s)

people wising to take an QRAVE test (English proficiency test)

Industry/Entity Type

Online

Colors
3276b5
0292cd

Requirements
Must have
• a place for enrollment and admin login for students
plovix
video
talvo, gatherly, chirrup logos
Nice to have
• a booking calender
Should not have
• too much clutter. must be clean and professional looking

```html
<!DOCTYPE html>
<html lang="en">
<head>
<meta charset="utf-8">
<title>QRAVE Online Tuition</title>
<link href="https://fonts.googleapis.com/css2?family=Raleway:wght@400;600;700;800&family=Open+Sans:wght@300;400;600;700&display=swap" rel="stylesheet">
<style>
:root{
  --blue:#3276b5;
  --sky:#0292cd;
  --navy:#1f3e8c;
  --ink:#333;
  --muted:#666;
  --pale:#f4f4f4;
  --line:#d8d8d8;
  --white:#fff;
}
*{box-sizing:border-box;margin:0;padding:0}
html,body{width:900px;height:1200px;overflow:hidden}
body{position:relative;font-family:"Open Sans",sans-serif;color:var(--ink);background:var(--white)}
.abs{position:absolute}
a{color:inherit;text-decoration:none}

/* header */
.site-header{left:0;top:0;width:900px;height:95px;background:linear-gradient(#f2f2f2,#fff)}
.brand{left:152px;top:18px}
.brand-name{font-family:"Raleway",sans-serif;font-weight:700;font-size:34px;color:var(--navy);letter-spacing:1px;display:flex;align-items:center;gap:8px;line-height:1}
.brand-dot{width:14px;height:14px;border-radius:50%;background:var(--navy)}
.brand-sub{font-size:11px;color:var(--navy);margin-left:52px;margin-top:2px}
.top-social{right:150px;top:15px;display:flex;gap:8px;font-size:9px;color:#444}
.top-social span{border:1px solid #555;border-radius:8px;padding:1px 5px}
.search{left:586px;top:45px;width:164px;height:20px;border:1px solid var(--line);background:#fff}
.search svg{position:absolute;right:3px;top:3px}
.search::before{content:"";position:absolute;right:19px;top:0;height:18px;border-left:1px solid var(--line)}

/* nav */
.main-nav{left:150px;top:80px;width:600px;height:28px;background:var(--blue);display:flex;z-index:2;font-size:8.5px;color:#fff}
.main-nav a{display:flex;align-items:center;padding:0 10px;border-right:1px solid rgba(255,255,255,.35)}
.main-nav a.active{background:#4a8bc6}
.main-nav a.login{margin-left:auto;width:114px;justify-content:center;background:var(--sky);font-size:11px;font-weight:600;border:none;letter-spacing:.5px}

/* hero */
.hero{left:0;top:95px;width:900px;height:274px}
.hero-photo{position:absolute;inset:0;background:linear-gradient(90deg,#8a8079 0%,#b9b4ae 30%,#d8dbe0 55%,#9fb4c8 75%,#6d6660 100%)}
.hero-title{left:152px;top:157px;font-family:"Raleway",sans-serif;font-weight:800;font-size:24px;color:var(--blue);letter-spacing:-.5px}
.hero-lead{left:155px;top:183px;font-size:12px;line-height:15px;color:#222;width:280px}
.hero-social{left:172px;top:240px;display:flex;gap:8px}
.hero-social span{width:36px;height:36px;border-radius:50%;border:2px solid var(--sky);background:rgba(255,255,255,.6);display:flex;align-items:center;justify-content:center;font-size:7.5px;color:var(--sky);font-weight:600}
.btn-contact{left:151px;top:295px;width:162px;height:28px;background:var(--sky);color:#fff;font-weight:700;font-size:15px;display:flex;align-items:center;justify-content:center;border-radius:2px}

/* welcome */
.welcome{left:0;top:369px;width:900px;height:80px;background:var(--pale)}
.welcome h1{position:absolute;left:155px;top:16px;font-family:"Raleway",sans-serif;font-weight:700;font-size:18px;color:var(--blue)}
.welcome p{position:absolute;left:160px;top:42px;width:570px;font-size:10.5px;line-height:13px;color:#333}

/* services */
.services{left:0;top:449px;width:900px;height:184px;background:var(--blue)}
.card{top:16px;width:194px}
.card-box{height:110px;background:#f0f0f0;border:1px solid #fff;text-align:center}
.card-box h2{font-family:"Raleway",sans-serif;font-size:11px;font-weight:700;color:var(--blue);margin-top:10px}
.card-art{width:70px;height:62px;margin:8px auto 0;border-radius:6px}
.card p{font-size:7px;line-height:9px;color:#dde8f4;margin:7px 5px 0}
.card .more{display:block;margin:11px 6px 0;font-size:7px;font-weight:700;color:#fff}

/* promise */
.promise{left:0;top:633px;width:900px;height:213px;border-bottom:1px solid var(--line)}
.promise .lead{position:absolute;left:155px;top:28px;font-size:12.5px;line-height:18px;font-weight:300;color:var(--sky)}
.promise ul{position:absolute;left:158px;top:76px;list-style:none;font-size:12px;font-weight:300;color:#333}
.promise li{line-height:18.5px;padding-left:12px;position:relative}
.promise li::before{content:"";position:absolute;left:0;top:6px;width:7px;height:7px;border:2px solid #222;border-radius:50%;box-sizing:border-box}
.community-art{left:576px;top:30px;width:160px;height:160px;border-radius:50% 50% 10px 10px;background:radial-gradient(circle at 50% 30%,#5d95c9,var(--blue))}

/* booking */
.booking h2{position:absolute;left:151px;top:866px;font-family:"Raleway",sans-serif;font-weight:700;font-size:17px;color:#444}
.booking .intro{position:absolute;left:151px;top:895px;width:236px;font-size:8.2px;line-height:10.8px;color:#777}
.field{left:413px;width:161px;height:17px;border:1px solid #ccc;background:#f7f7f7;font-size:7.5px;color:#999;padding:4px 6px;border-radius:2px}
.btn-book{left:494px;top:995px;width:80px;height:18px;background:var(--sky);color:#fff;font-size:7.5px;font-weight:700;display:flex;align-items:center;justify-content:center;border-radius:2px}
.calendar{left:589px;top:878px;width:162px;height:135px;background:#eee;border-radius:2px}
.cal-head{display:grid;grid-template-columns:repeat(7,1fr);height:19px;background:#e2e2e2;font-size:6.5px;color:var(--sky);align-items:center;text-align:center;padding:0 6px}
.cal-grid{display:grid;grid-template-columns:repeat(7,16px);gap:4px 4.3px;padding:8px 12px}
.cal-grid span{height:15px;font-size:6px;display:flex;align-items:center;justify-content:center;color:var(--blue)}
.cal-grid span.on{background:#697c8e;color:#fff;border-radius:2px}

/* footer */
.site-footer{left:0;top:1038px;width:900px;height:118px;background:var(--blue);color:#fff}
.foot-col{top:16px}
.foot-col h3{font-family:"Raleway",sans-serif;font-size:10.5px;font-weight:700;margin-bottom:10px}
.foot-col li{list-style:none;font-size:9px;line-height:14.5px}
.foot-brand{left:624px;top:30px}
.foot-brand .brand-name{color:var(--navy)}
.foot-brand .brand-sub{color:var(--navy)}
.legal{left:0;top:1156px;width:900px;height:44px;background:var(--sky);color:#fff;font-size:7.5px}
.legal .links{position:absolute;left:151px;top:18px;word-spacing:2px}
.legal .copy{position:absolute;right:150px;top:19px}
</style>
</head>
<body>

<header class="abs site-header"></header>
<div class="abs brand">
  <div class="brand-name"><span class="brand-dot"></span>QRAVE</div>
  <div class="brand-sub">Online Tuition</div>
</div>
<div class="abs top-social"><span>chirrup</span><span>proflink</span><span>gatherly</span></div>
<div class="abs search">
  <svg width="12" height="12" viewBox="0 0 12 12"><circle cx="5" cy="5" r="3.5" fill="none" stroke="#999" stroke-width="1"/><line x1="7.5" y1="7.5" x2="10.5" y2="10.5" stroke="#999"/></svg>
</div>

<nav class="abs main-nav">
  <a class="active" href="#">Home</a>
  <a href="#">Tutorial Packages</a>
  <a href="#">Weekly Tips and Comments</a>
  <a href="#">Reading</a>
  <a href="#">Speaking</a>
  <a href="#">Listening</a>
  <a href="#">Writing</a>
  <a class="login" href="#">LOGIN</a>
</nav>

<section class="abs hero">
  <div class="hero-photo" role="img" aria-label="Photo of a smiling student working on a laptop at an outdoor table"></div>
</section>
<div class="abs hero-title">ONLINE QRAVE TUTION</div>
<div class="abs hero-lead">PROFSSIONAL HELP FOR PEOPLE TAKING AN QRAVE TEST</div>
<div class="abs hero-social"><span>gatherly</span><span>talvo</span><span>chirrup</span></div>
<a class="abs btn-contact" href="#">CONTACT US</a>

<section class="abs welcome">
  <h1>Welcome To QRAVE Online Tuition</h1>
  <p>International English Tuition We put our customers first. We listen to you and help you find what you need. If you want help...</p>
</section>

<section class="abs services">
  <article class="abs card" style="left:150px">
    <div class="card-box"><h2>QRAVE Online Tuition</h2><div class="card-art" role="img" aria-label="Illustration of a globe with an e-learning label and cursor" style="background:radial-gradient(circle,#6fb2e0,#2f74b6)"></div></div>
    <p>Lorem ipsum dolor sit amet, conseer apiscing elit, sed diam nonummy nib...</p>
    <a class="more" href="#">READMORE +</a>
  </article>
  <article class="abs card" style="left:353px">
    <div class="card-box"><h2>Tutorial Packages</h2><div class="card-art" role="img" aria-label="Illustration of a figure beside a tutorials box and disc" style="background:linear-gradient(135deg,#e8e8e8,#d9a94a 60%,#c0392b)"></div></div>
    <p>Lorem ipsum dolor sit amet, conseer adipiscing elit, sed diam nonummy nib...</p>
    <a class="more" href="#">READMORE +</a>
  </article>
  <article class="abs card" style="left:557px">
    <div class="card-box"><h2>Weekly Tips and Comments</h2><div class="card-art" role="img" aria-label="Illustration of speech bubbles over a computer mouse" style="background:linear-gradient(135deg,#59b8e6,#f2d34a 55%,#444)"></div></div>
    <p>Lorem ipsum dolor sit amet, conseer adipiscing elit, sed diam nonummy nib...</p>
    <a class="more" href="#">READMORE +</a>
  </article>
</section>

<section class="abs promise">
  <p class="lead">We put you first. We listen to you and help you find what you need.<br>If you want help in passing an QRAVE test, we can help you with:</p>
  <ul>
    <li>Lessons in reading, writing, listening and speaking</li>
    <li>Professional teacher feedback and tips.</li>
    <li>Talvo and practice with native speakers.</li>
    <li>Quick Turnaround.</li>
    <li>Friendly and Approachable teachers.</li>
  </ul>
  <div class="abs community-art" role="img" aria-label="Blue illustration of a group of people under an arch"></div>
</section>

<section class="booking">
  <h2>BOOKING CALENDER</h2>
  <p class="intro">Lorem ipsum dolor sit amet, consectetuer adipiscing elit, sed diam nonummy nibh euismod tincidunt ut laoreet dre magna aliquam erat volutpat. Ut wisi enim ad minim veniam, qostrud exerci tation ullamcorper suscipit lobortis nisl ut aliquip ex ea commodo consequat. Duis autem vel eum iritytigure dolor in hendrerit in vulputate velit esse molestie consiquat, vel illum dolore eu feugiat nulla facilisis at vero eros et accuan et iusto odio dignissim qui blandit praesent luptatum zzril dnit augue duis dolore te feugait nulla facilisi.</p>
  <div class="abs field" style="top:879px">First Name</div>
  <div class="abs field" style="top:902px">Last Name</div>
  <div class="abs field" style="top:925px">E-mail</div>
  <div class="abs field" style="top:948px">Phone</div>
  <div class="abs field" style="top:971px">Address</div>
  <a class="abs btn-book" href="#">BOOK NOW</a>
  <div class="abs calendar">
    <div class="cal-head"><span>Su</span><span>Mo</span><span>Tu</span><span>We</span><span>Th</span><span>Fr</span><span>Sa</span></div>
    <div class="cal-grid">
      <span>1</span><span>2</span><span>3</span><span class="on">4</span><span class="on">5</span><span class="on">6</span><span class="on">7</span>
      <span class="on">8</span><span class="on">9</span><span class="on">10</span><span class="on">11</span><span class="on">12</span><span class="on">13</span><span class="on">14</span>
      <span class="on">15</span><span class="on">16</span><span class="on">17</span><span class="on">18</span><span class="on">19</span><span class="on">20</span><span class="on">21</span>
      <span class="on">22</span><span class="on">23</span><span class="on">24</span><span class="on">25</span><span class="on">26</span><span class="on">27</span><span class="on">28</span>
      <span class="on">29</span><span class="on">30</span><span class="on">31</span>
    </div>
  </div>
</section>

<footer class="abs site-footer">
  <div class="abs foot-col" style="left:151px"><h3>Our Courses</h3><ul><li>QRAVE Express</li><li>QRAVE Master</li><li>QRAVE Master Plus</li></ul></div>
  <div class="abs foot-col" style="left:315px"><h3>More Info</h3><ul><li>FAQ</li><li>Agent FAQ</li><li>About Us</li></ul></div>
  <div class="abs foot-col" style="left:458px"><h3>Social Media</h3><ul><li>Gatherly</li><li>Chirrup</li><li>Proflink</li><li>Talvo</li></ul></div>
  <div class="abs foot-brand">
    <div class="brand-name"><span class="brand-dot"></span>QRAVE</div>
    <div class="brand-sub">Online Tuition</div>
  </div>
</footer>
<div class="abs legal">
  <span class="links">Terms &amp; Conditions &nbsp;| &nbsp;Privacy Statement &nbsp;| &nbsp;Sitemap</span>
  <span class="copy">© Harbourline Ltd. All Rights Reserved.</span>
</div>

</body>
</html>
```